Book Cover:Legend of Crystals-particularly diamonds from Canada. Arctic diamonds pure & clean
Inside the remarkable northern search for pure stones
The discovery of diamonds in Canada and how it changed the diamond industry
This book is about the the Legend of Crystals. It then goes to talk about how people have become aware of conflict diamonds and started to prefer diamonds that are from NON conflict areas LIKE CANADA.
Jewelry
Corporate. and also for people who are thinking of buying a diamond in the near future
I need a book cover that captures the breath taking Canadian arctic with some kind of a diamond image. when someone looks at the book, they will want to buy only a diamond from canada. Canada's pure and clean image has to be displayed in the cover.

```html
<!DOCTYPE html>
<html lang="en">
<head>
<meta charset="utf-8">
<title>Legend of Crystals — Book Cover Wraps</title>
<link href="https://fonts.googleapis.com/css2?family=Cinzel:wght@400;600&family=Cormorant+Garamond:ital,wght@0,500;1,400;1,500&display=swap" rel="stylesheet">
<style>
  :root {
    --page: #ffffff;
    --ink-black: #0b0b0c;
    --paper-white: #f4f6f8;
    --muted-white: #c9cdd2;
    --sky-top: #0e3d8c;
    --sky-mid: #3f78c4;
    --sky-low: #a9c6e6;
    --sea-deep: #1d4f8f;
    --ice: #e9f1f8;
    --band-navy: #07142e;
    --band-navy-2: #0f2450;
  }
  * { box-sizing: border-box; margin: 0; padding: 0; }
  html, body {
    width: 1200px; height: 413px; overflow: hidden;
    background: var(--page);
  }
  .canvas { position: relative; width: 1200px; height: 413px; }
  .wrap {
    position: absolute; top: 19px; width: 564px; height: 377px;
    display: flex;
  }
  .wrap--legend { left: 12px; }
  .wrap--polar { left: 620px; }

  /* Back cover */
  .back-cover {
    width: 257px; height: 100%;
    background: var(--ink-black);
    color: var(--muted-white);
    padding: 22px 20px 0 20px;
  }
  .back-cover__title {
    font-family: "Cormorant Garamond", serif;
    font-weight: 500;
    font-size: 19px;
    color: var(--paper-white);
    text-align: center;
    margin-bottom: 12px;
    letter-spacing: 0.3px;
  }
  .back-cover__quote {
    font-family: "Cormorant Garamond", serif;
    font-style: italic;
    font-size: 10.6px;
    line-height: 1.42;
    margin-bottom: 14px;
  }

  /* Spine */
  .spine {
    width: 50px; height: 100%;
    background: var(--ink-black);
    border-left: 1px solid #222;
    display: flex; align-items: center; justify-content: center;
  }
  .spine__title {
    writing-mode: vertical-rl;
    font-family: "Cinzel", serif;
    font-size: 17px;
    letter-spacing: 1.5px;
    color: var(--paper-white);
    white-space: nowrap;
  }

  /* Front cover */
  .front-cover {
    position: relative;
    width: 257px; height: 100%;
    overflow: hidden;
    background: linear-gradient(180deg, var(--sky-top) 0%, var(--sky-mid) 30%, var(--sky-low) 52%, var(--sea-deep) 72%, var(--band-navy-2) 82%);
  }
  .front-cover__author {
    position: absolute; top: 12px; left: 0; right: 0;
    text-align: center;
    font-family: "Cinzel", serif;
    font-size: 12px;
    letter-spacing: 1.2px;
    color: var(--paper-white);
  }
  .front-cover__scene {
    position: absolute; left: 0; right: 0; top: 70px; height: 200px;
    background:
      radial-gradient(ellipse 60% 22% at 55% 48%, var(--ice) 0%, rgba(233,241,248,0.55) 45%, rgba(233,241,248,0) 75%),
      linear-gradient(180deg, rgba(169,198,230,0) 0%, var(--sky-low) 38%, var(--sea-deep) 62%, rgba(15,36,80,0.9) 100%);
  }
  .front-cover__title {
    position: absolute; left: 0; right: 0;
    text-align: center;
    color: #ffffff;
    text-shadow: 0 1px 3px rgba(0,20,60,0.55);
  }
  .title-legend { top: 100px; }
  .title-legend .title-line--big {
    font-family: "Cinzel", serif; font-weight: 600;
    font-size: 38px; line-height: 1.0; display: block;
  }
  .title-legend .title-line--small {
    font-family: "Cormorant Garamond", serif; font-style: italic; font-weight: 500;
    font-size: 30px; line-height: 1.0; display: block;
  }
  .title-polar { top: 112px; }
  .title-polar .title-line--big {
    font-family: "Cinzel", serif; font-weight: 600;
    font-size: 29px; line-height: 1.12; display: block; letter-spacing: 0.5px;
  }
  .front-cover__band {
    position: absolute; left: 0; right: 0; bottom: 0; height: 80px;
    background: linear-gradient(180deg, var(--band-navy-2) 0%, var(--band-navy) 100%);
    display: flex; align-items: center; justify-content: center;
  }
  .front-cover__tagline {
    font-family: "Cinzel", serif;
    font-size: 11px;
    line-height: 1.45;
    letter-spacing: 0.6px;
    color: var(--paper-white);
    text-align: center;
  }
</style>
</head>
<body>
<main class="canvas">

  <section class="wrap wrap--legend" aria-label="Legend of Crystals book cover">
    <div class="back-cover">
      <h2 class="back-cover__title">Legend of Crystals</h2>
      <p class="back-cover__quote">“Diamond trade remains a very quiet world, yet few stones travel a path as clean as those lifted from the northern ice. This is the story of how Canada changed what a diamond means.”</p>
      <p class="back-cover__quote">“The emergence of Canada's diamond industry stands as the most significant event in the trade in many years, offering buyers a source they can trust without question.”</p>
      <p class="back-cover__quote">“The discovery of diamonds in Canada is a major turning point in the industry, setting a new standard for purity, ethics and the value of a natural stone.”</p>
    </div>
    <div class="spine"><span class="spine__title">LEGEND OF CRYSTALS</span></div>
    <div class="front-cover">
      <p class="front-cover__author">By Jethro Malvick</p>
      <div class="front-cover__scene" role="img" aria-label="Arctic sea with a floating iceberg under a blue sky"></div>
      <h1 class="front-cover__title title-legend">
        <span class="title-line--big">Legend</span>
        <span class="title-line--small">of</span>
        <span class="title-line--big">Crystals</span>
      </h1>
      <div class="front-cover__band">
        <p class="front-cover__tagline">INSIDE THE REMARKABLE<br>NORTHERN SEARCH FOR PURE STONES</p>
      </div>
    </div>
  </section>

  <section class="wrap wrap--polar" aria-label="Polar Clear Stones book cover">
    <div class="back-cover">
      <h2 class="back-cover__title">Polar Clear Stones</h2>
      <p class="back-cover__quote">“Diamond trade remains a very quiet world, yet few stones travel a path as clean as those lifted from the northern ice. This is the story of how Canada changed what a diamond means.”</p>
      <p class="back-cover__quote">“The emergence of Canada's diamond industry stands as the most significant event in the trade in many years, offering buyers a source they can trust without question.”</p>
      <p class="back-cover__quote">“The discovery of diamonds in Canada is a major turning point in the industry, setting a new standard for purity, ethics and the value of a natural stone.”</p>
    </div>
    <div class="spine"><span class="spine__title">POLAR CLEAR STONES</span></div>
    <div class="front-cover">
      <p class="front-cover__author">By Jethro Malvick</p>
      <div class="front-cover__scene" role="img" aria-label="Arctic sea with a floating iceberg under a blue sky"></div>
      <h1 class="front-cover__title title-polar">
        <span class="title-line--big">POLAR CLEAR</span>
        <span class="title-line--big">STONES</span>
      </h1>
      <div class="front-cover__band">
        <p class="front-cover__tagline">INSIDE THE REMARKABLE<br>NORTHERN SEARCH FOR PURE STONES</p>
      </div>
    </div>
  </section>

</main>
</body>
</html>
```